Eycatcher Flyer
Bin sehr zufrieden mit der Arbeit von diesem Designer. Auch mehrere Änderungswünsche wurden prompt ausgeführt. Unkompliziert und schnell.
Zielgruppe
Infos auf www.sonnenpfad.ch
Lebensberatung, Seminare, persönliche Weiterbildung,Medium
Aufgabenstellung
Suche ein Design für einen coolen, modernen, mystischen exklusiven(Image) Flyer. Format A4 Längs gefaltet (Endformat A5).
Flyer Titel Liebe dein Leben - Liebe dich selbst eventuell auch auf englisch love yourself and celebrates your life
oder vielleicht hat jemand noch einen besseren Slogan Vorschlag
Habe im Anhang ein Dokument mit Text kann ganz oder auszugweise verwendet werden. (Handelt sich um einen ersten Entwurf mögliche Rechtschreibfehler enthalten)
Ansonsten Inputs aus der Hp holen.
Lieblingsfarben Rot,Pink,Giftgrün,Gold,Schwarz, Gelb,

```html
<!DOCTYPE html>
<html lang="de">
<head>
<meta charset="utf-8">
<title>Annahme – Wertschätzung – Achtung</title>
<link rel="stylesheet" href="https://fonts.googleapis.com/css2?family=Didact+Gothic&family=Parisienne&display=swap">
<style>
  :root {
    --paper: #ffffff;
    --ink: #8a5a2c;
    --ink-soft: #9a6a3a;
    --initial: #a57640;
    --dot: #b08659;
    --fold: #c9c2bb;
    --photo-dark: #a88a7a;
    --photo-mid: #d8bcae;
    --photo-light: #f3dfcf;
    --glow: #ffe9c8;
  }
  * { margin: 0; padding: 0; box-sizing: border-box; }
  html, body { width: 1200px; height: 847px; overflow: hidden; background: var(--paper); }
  .spread {
    position: relative; width: 1200px; height: 847px; background: var(--paper);
    font-family: "Didact Gothic", "Century Gothic", sans-serif; color: var(--ink);
    font-size: 15px; line-height: 21px;
  }
  .fold { position: absolute; left: 600px; top: 0; width: 1px; height: 847px; background: var(--fold); }
  .text { position: absolute; }
  .drop {
    font-size: 37px; line-height: 20px; color: var(--initial);
    float: left; margin: 8px 3px 0 0;
  }
  .intro { left: 44px; top: 54px; width: 520px; }
  .snail-photo { position: absolute; left: 163px; top: 182px; width: 272px; height: 272px; }
  .headline {
    position: absolute; left: 50px; top: 486px; width: 520px; text-align: center;
    font-size: 19px; font-weight: 400; color: var(--ink-soft); letter-spacing: 0.3px;
  }
  .headline .script { font-family: "Parisienne", cursive; font-size: 40px; color: var(--initial); }
  .tagline {
    position: absolute; left: 52px; top: 534px; width: 520px; text-align: center; font-size: 14.5px;
  }
  .roots { left: 44px; top: 582px; width: 530px; }
  .roots p + p { margin-top: 21px; }
  .hero-photo { position: absolute; left: 601px; top: 0; width: 599px; height: 243px; }
  .values { left: 644px; top: 270px; width: 540px; }
  .values p + p { margin-top: 21px; }
  .questions { position: absolute; left: 644px; top: 541px; width: 530px; list-style: none; }
  .questions li { padding-left: 14px; text-indent: -14px; }
  .questions li::before { content: "• "; }
  .questions li .wrap { padding-left: 14px; }
  .closing { position: absolute; left: 640px; top: 690px; width: 550px; height: 130px; }
  .closing .big-g {
    position: absolute; left: 0; top: 0; font-family: "Parisienne", cursive;
    font-size: 96px; line-height: 120px; color: var(--initial);
  }
  .closing p { position: absolute; left: 72px; top: 36px; }
  .closing .sr { position: absolute; width: 1px; height: 1px; overflow: hidden; clip: rect(0 0 0 0); }
</style>
</head>
<body>
<main class="spread">
  <div class="fold"></div>

  <section class="page-left">
    <p class="text intro"><span class="drop">W</span>ir rennen und tun, wir sind oft so gefangen im Rad des<br>Aktivismus, dass wir ganz vergessen zu sein. Wir sind so<br>beshäftigt damit etwas zu verändern, dass wir dass wir<br>vollkommen vergessen unser Leben zu geniessen und mit<br>Liebe zu erfüllen.</p>

    <svg class="snail-photo" viewBox="0 0 228 228" role="img" aria-label="Fotografie: Schneckenhaus auf spiegelnder Fläche in Sepiatönen, runder Ausschnitt mit Punktrahmen">
      <defs>
        <radialGradient id="snailTone" cx="50%" cy="45%" r="55%">
          <stop offset="0%" stop-color="#f6e6d8"/>
          <stop offset="70%" stop-color="#e4c8b3"/>
          <stop offset="100%" stop-color="#cfa78d"/>
        </radialGradient>
      </defs>
      <circle cx="114" cy="114" r="106" fill="url(#snailTone)"/>
      <circle cx="114" cy="114" r="110" fill="none" stroke="var(--dot)" stroke-width="3" stroke-linecap="round" stroke-dasharray="0 8.6"/>
    </svg>

    <h1 class="headline"><span class="script">A</span>nnahme – <span class="script">W</span>ertschätzung – <span class="script">A</span>chtung</h1>
    <p class="tagline">...altmodische, fast vergessene Worte.</p>

    <div class="text roots">
      <p><span class="drop">D</span>och diese Worte haben Kraft. Es sind Worte mit Wurzeln,<br>Worte die einem eine Heimat geben. Eine Heimat in sich<br>selber und eine Heimat im Leben. Eine Heimat die<br>unabhängig von geografischen Orten und äusseren<br>Umständen ist.</p>
      <p>Gegebenheiten akzeptieren. Körperliche ebenso<br>wie Psychische. Wir sind was wir sind<br>Menschen mit Stärken und Schwächen.</p>
    </div>
  </section>

  <section class="page-right">
    <svg class="hero-photo" viewBox="0 0 599 243" preserveAspectRatio="none" role="img" aria-label="Fotografie: Perlmuttkugeln und leuchtendes Windlicht in warmem Licht">
      <defs>
        <linearGradient id="heroBase" x1="0" y1="0" x2="0" y2="1">
          <stop offset="0%" stop-color="var(--photo-dark)"/>
          <stop offset="55%" stop-color="var(--photo-mid)"/>
          <stop offset="100%" stop-color="#c7a593"/>
        </linearGradient>
        <radialGradient id="heroGlow" cx="80%" cy="55%" r="35%">
          <stop offset="0%" stop-color="var(--glow)"/>
          <stop offset="100%" stop-color="var(--glow)" stop-opacity="0"/>
        </radialGradient>
        <radialGradient id="heroPearl" cx="20%" cy="55%" r="22%">
          <stop offset="0%" stop-color="var(--photo-light)"/>
          <stop offset="100%" stop-color="var(--photo-light)" stop-opacity="0"/>
        </radialGradient>
      </defs>
      <rect width="599" height="243" fill="url(#heroBase)"/>
      <rect width="599" height="243" fill="url(#heroPearl)"/>
      <rect width="599" height="243" fill="url(#heroGlow)"/>
    </svg>

    <div class="text values">
      <p><span class="drop">W</span>ertschätzen was ist und mit Achtung verändern was<br>möglich und sinnvoll ist. Annehmen und akzeptieren was ist,<br>und so bleiben will wie es ist.</p>
      <p>Wenn Du nicht weißt wo du bist, kannst du auch nicht wissen<br>wo du landest wenn du dich auf den Weg machst. Selbst<br>dann, wenn du die Himmelsrichtungen erkennst oder eine<br>Karte besitzt. Erst musst du deinen Ausgangsort kennen.</p>
      <p>Wenn du Dein Ziel kennst musst du auch wissen wo du jetzt<br>stehst. So kannst du den besten Weg zur Erreichung deines<br>Zieles finden, und die für dich optimale Reiseroute planen.</p>
    </div>

    <ul class="questions">
      <li>Was habe ich?</li>
      <li>Wo will ich hin?</li>
      <li>Warum?</li>
      <li>Was trägt es zu meinem Leben bei wenn ich dieses Ziel<br><span class="wrap">erreiche?</span></li>
      <li>Worauf verzichte ich wenn ich dieses Ziel erreiche?</li>
    </ul>

    <div class="closing">
      <span class="big-g" aria-hidden="true">G</span>
      <p><span class="sr">G</span>anz oft sind wir so damit beschäftigt jemand zu werden,<br>dass wir ganz vergessen jemand zu sein...</p>
    </div>
  </section>
</main>
</body>
</html>
```